Forensic Document Examiner, looking for contemporary update to my stationery design.

Looking for professional, classy logo design for stationery and business cards. My current stationery and business card is attached.I believe a logo image makes a header section interesting, so an intriguing design of a pen, feathered pen, microscope, magnifying glass, etc., would be appropriate. I have been in the business for over 30 years. I leave ideas to the imagination of the designer.My work involves mainly, the comparison of signatures and handwriting. I also resolve alterations, obliterations, and work as shown on my website: www.documentexaminer.infoThe image produced will be printed on quality white stationery and envelopes. The stationery will be photocopied by my clients, so the images should be reproducible. The business cards may be designed in other than white.

Target Market(s)

Attorneys

Font styles to use
Sans Serif

Colors

Designer to choose colors to be used in the design.

Requirements
Must have
• Image suitable for white stationery and photocopying.
• Classy logo and image; no casual fonts.
Nice to have
• Intriguing, contemporary design incorporating a relevant logo to my work.

```html
<!DOCTYPE html>
<html lang="en">
<head>
<meta charset="utf-8">
<title>Martin R. Hale — Stationery</title>
<link href="https://fonts.googleapis.com/css2?family=Lato:wght@300;400;700&family=Pinyon+Script&display=swap" rel="stylesheet">
<style>
:root{
  --bg:#e9eaec;
  --paper:#ffffff;
  --ink:#3a3a44;
  --ink-soft:#55565f;
  --navy:#22223a;
  --gold:#e6d34a;
  --forest:#4a5a33;
  --forest-deep:#36432a;
  --sky:#6d7c88;
  --river:#8fa6bd;
}
*{box-sizing:border-box;margin:0;padding:0}
html,body{width:1200px;height:960px;overflow:hidden;background:var(--bg)}
body{font-family:"Lato",sans-serif;color:var(--ink);position:relative}

.sheet{position:absolute;background:var(--paper);box-shadow:0 2px 6px rgba(0,0,0,.12);overflow:hidden}
.sheet::after{content:"";position:absolute;left:0;right:0;bottom:0;height:5px;background:var(--navy)}

.scenery{position:absolute;top:0;right:0;
  background:
    linear-gradient(to right,var(--paper) 0%,rgba(255,255,255,.75) 18%,rgba(255,255,255,0) 45%),
    linear-gradient(to bottom,var(--sky) 0%,var(--forest-deep) 22%,var(--forest) 42%,var(--river) 62%,rgba(220,228,235,.6) 82%,rgba(255,255,255,0) 100%);}

.wordmark{position:absolute;display:flex;align-items:center;gap:8px}
.wordmark .dot{border-radius:50%;background:#fff;flex:none}
.wordmark .name{font-weight:700;color:#fff;letter-spacing:.08em;text-transform:uppercase;line-height:1;white-space:nowrap}
.tagline{color:var(--gold);font-weight:700;letter-spacing:.02em;white-space:nowrap}

/* letterhead */
.letterhead{left:40px;top:84px;width:560px;height:792px}
.letterhead .scenery{width:100%;height:330px}
.letterhead .wordmark{left:36px;top:40px}
.letterhead .dot{width:14px;height:14px}
.letterhead .name{font-size:26px}
.letterhead .tagline{position:absolute;left:58px;top:74px;font-size:12px}
.letter{position:absolute;left:56px;top:236px;right:48px;font-size:10.5px;line-height:1.45;color:var(--ink-soft);font-weight:300}
.letter .date{margin-bottom:12px}
.letter .to strong{font-weight:700;color:var(--ink)}
.letter .to{margin-bottom:12px}
.letter .greet{margin-bottom:10px}
.letter p.body{margin-bottom:9px;text-align:justify}
.letter .closing{margin-top:14px}
.signature{font-family:"Pinyon Script",cursive;font-size:24px;line-height:1.2;color:var(--ink);margin-top:4px}
.contacts{list-style:none;font-size:11.5px;line-height:1.45;color:var(--ink)}
.contacts li{display:flex;align-items:center;gap:7px}
.contacts svg{width:10px;height:10px;fill:var(--navy);flex:none}
.letterhead .contacts{position:absolute;left:40px;bottom:28px}
.letterhead .postal{position:absolute;right:40px;bottom:28px;font-size:12px;line-height:1.4;text-align:right}

/* business cards */
.card{position:absolute;width:250px;height:143px;background:var(--navy);box-shadow:0 2px 6px rgba(0,0,0,.18);color:#fff;overflow:hidden}
.card-back{left:640px;top:84px}
.card-front{left:910px;top:84px}
.card .dot{width:9px;height:9px}
.card-back .wordmark{left:16px;top:40px;gap:6px}
.card-back .name{font-size:14px;line-height:1.1}
.card-back .tagline{position:absolute;left:31px;top:76px;font-size:7px}
.card-back .rule{position:absolute;left:142px;top:26px;width:1px;height:92px;background:var(--gold)}
.card-back .details{position:absolute;left:150px;top:30px;font-size:6.5px;line-height:1.45;white-space:nowrap}
.card-back .details .who{color:var(--gold);font-weight:700;font-size:8.5px}
.card-back .details svg{width:6px;height:6px;fill:var(--gold);margin-right:3px;vertical-align:-0.5px}
.card-front .wordmark{left:38px;top:36px}
.card-front .name{font-size:18px}
.card-front .tagline{position:absolute;left:55px;top:60px;font-size:8.5px}
.card-front .blurb{position:absolute;left:18px;right:18px;top:96px;font-size:6.8px;line-height:1.5;text-align:center;color:#d8d8e2}

/* envelope */
.envelope{left:640px;top:260px;width:520px;height:260px}
.envelope .scenery{width:78%;height:170px}
.envelope .wordmark{left:140px;top:26px}
.envelope .dot{width:10px;height:10px}
.envelope .name{font-size:19px}
.envelope .tagline{position:absolute;left:158px;top:50px;font-size:9px}
.envelope .return{position:absolute;left:26px;top:118px;font-size:9.5px;line-height:1.4}
.envelope .return .street{margin-bottom:6px}
.envelope .contacts{font-size:9.5px}
.envelope .contacts svg{width:8px;height:8px}
.window{position:absolute;right:26px;bottom:30px;width:190px;height:88px;border-radius:10px;background:#e4e5e7;border:1px solid #d6d7da}
</style>
</head>
<body>

<svg width="0" height="0" style="position:absolute" aria-hidden="true">
  <symbol id="i-phone" viewBox="0 0 24 24"><path d="M6.6 10.8a15 15 0 0 0 6.6 6.6l2.2-2.2a1 1 0 0 1 1-.25 11.4 11.4 0 0 0 3.6.57 1 1 0 0 1 1 1V20a1 1 0 0 1-1 1A17 17 0 0 1 3 4a1 1 0 0 1 1-1h3.5a1 1 0 0 1 1 1c0 1.250.2 2.450.57 3.6a1 1 0 0 1-.25 1z"/></symbol>
  <symbol id="i-fax" viewBox="0 0 24 24"><path d="M6 2h9l3 3v4H6zM4 10h16a2 2 0 0 1 2 2v6h-4v4H6v-4H2v-6a2 2 0 0 1 2-2zm4 7v3h8v-3z"/></symbol>
  <symbol id="i-mail" viewBox="0 0 24 24"><path d="M2 5h20v14H2zm2 2v.4l8 5.2 8-5.2V7zm0 2.8V17h16V9.8l-8 5.2z"/></symbol>
  <symbol id="i-globe" viewBox="0 0 24 24"><path d="M12 2a10 10 0 1 0 0 20 10 10 0 0 0 0-20zm6.9 6h-3a15 15 0 0 0-1.4-3.6A8 8 0 0 1 18.9 8zM12 4c.8 1.2 1.5 2.5 1.9 4h-3.8c.4-1.5 1.1-2.8 1.9-4zM4.3 14a8 8 0 0 1 0-4h3.4a16 16 0 0 0 0 4zm.8 2h3a15 15 0 0 0 1.4 3.6A8 8 0 0 1 5.1 16zm3-8h-3a8 8 0 0 1 4.4-3.6A15 15 0 0 0 8.1 8zM12 20c-.8-1.2-1.5-2.5-1.9-4h3.8c-.4 1.5-1.1 2.8-1.9 4zm2.3-6H9.7a14 14 0 0 1 0-4h4.6a14 14 0 0 1 0 4zm.2 5.6a15 15 0 0 0 1.4-3.6h3a8 8 0 0 1-4.4 3.6zm1.8-5.6a16 16 0 0 0 0-4h3.4a8 8 0 0 1 0 4z"/></symbol>
</svg>

<!-- Letterhead -->
<section class="sheet letterhead">
  <div class="scenery" role="img" aria-label="Photograph of a tree-lined river under a cloudy sky, fading into white"></div>
  <div class="wordmark"><span class="dot"></span><span class="name">Martin R. Hale</span></div>
  <div class="tagline">Forensic Document Examiner</div>

  <div class="letter">
    <div class="date">01 January 2050</div>
    <div class="to"><strong>Company (Pvt) Ltd.</strong><br>PO Box 2210 Elmford St<br>Sample City Country 2210</div>
    <div class="greet">Dear Daniel Orwell,</div>
    <p class="body">Lorem ipsum dolor sit amet, consectetuer adipiscing elit, sed diam nonummy nibh euismod tincidunt ut laoreet dolore magna aliquam erat volutpat. Ut wisi enim ad minim veniam, quis nostrud exerci tation ullamcorper suscipit lobortis nisl ut aliquip ex ea commodo consequat. Duis dolore te feugait nulla facilisi. Nam liber tempor cum soluta nobis eleifend option congue nihil imperdiet doming id quod mazim placerat facer possim assum. Lorem ipsum dolor sit amet, consectetuer adipiscing elit, sed diam nonummy nibh euismod tincidunt ut laoreet dolore magna aliquam erat volutpat. Ut wisi enim ad minim veniam, quis nostrud exerci tation ullamcorper suscipit lobortis nisl ut aliquip ex ea commodo consequat.</p>
    <p class="body">Consectetuer adipiscing elit, sed diam nonummy nibh euismod tincidunt ut laoreet dolore magna aliquam erat volutpat. Ut wisi enim ad minim veniam, quis nostrud exerci tation ullamcorper suscipit lobortis nisl ut aliquip ex ea commodo consequat. Consectetuer adipiscing elit, sed diam nonummy nibh euismod tincidunt ut laoreet dolore magna aliquam erat volutpat.</p>
    <p class="body">Consectetuer adipiscing elit, sed diam nonummy nibh euismod tincidunt ut laoreet dolore magna aliquam erat volutpat. Ut wisi enim ad minim veniam, quis nostrud exerci tation ullamcorper suscipit lobortis nisl ut aliquip ex ea commodo consequat.</p>
    <div class="closing">Sincerely Yours</div>
    <div class="signature">Graham Lyle Porter</div>
  </div>

  <ul class="contacts">
    <li><svg><use href="#i-phone"/></svg>(555) 014-2290</li>
    <li><svg><use href="#i-fax"/></svg>(555) 014-2290</li>
    <li><svg><use href="#i-mail"/></svg>mhale@quillverity.example</li>
    <li><svg><use href="#i-globe"/></svg>www.quillverity.example</li>
  </ul>
  <div class="postal">PO Box 4120<br>Salem OR 97301</div>
</section>

<!-- Business card: details side -->
<section class="card card-back">
  <div class="wordmark"><span class="dot"></span><span class="name">Martin R.<br>Hale</span></div>
  <div class="tagline">Forensic Document Examiner</div>
  <div class="rule"></div>
  <div class="details">
    <div class="who">Martin R. Hale</div>
    <div>Forensic Document Examiner</div>
    <div style="margin-top:4px">PO Box 4120<br>Salem OR 97301</div>
    <div><svg><use href="#i-phone"/></svg>(555) 014-2290</div>
    <div><svg><use href="#i-fax"/></svg>(555) 014-2290</div>
    <div><svg><use href="#i-mail"/></svg>mhale@quillverity.example</div>
    <div><svg><use href="#i-globe"/></svg>www.quillverity.example</div>
  </div>
</section>

<!-- Business card: brand side -->
<section class="card card-front">
  <div class="wordmark"><span class="dot"></span><span class="name">Martin R. Hale</span></div>
  <div class="tagline">Forensic Document Examiner</div>
  <p class="blurb">Full service laboratory, specializing in handwriting comparisons.<br>Obliterations, alterations, indented writing recovery, etc.</p>
</section>

<!-- Envelope -->
<section class="sheet envelope">
  <div class="scenery" role="img" aria-label="Photograph of a tree-lined river under a cloudy sky, fading into white"></div>
  <div class="wordmark"><span class="dot"></span><span class="name">Martin R. Hale</span></div>
  <div class="tagline">Forensic Document Examiner</div>
  <div class="return">
    <div class="street">718 Birchwood Lane<br>Salem, OR 97301</div>
    <ul class="contacts">
      <li><svg><use href="#i-phone"/></svg>(555) 014-2290</li>
      <li><svg><use href="#i-fax"/></svg>(555) 014-2290</li>
      <li><svg><use href="#i-mail"/></svg>mhale@quillverity.example</li>
      <li><svg><use href="#i-globe"/></svg>www.quillverity.example</li>
    </ul>
  </div>
  <div class="window"></div>
</section>

</body>
</html>
```